Coloring Book Cover for Adults

I'd like a unique book cover design for a coloring book we are making for adults. The book cover is for an 8.5"x11" book. I need both the front and back cover created. We will want to include some text about the book on the back cover so there should be room for that. It will be less than 100 words.

1) The title is:

Hush Up and Shade, D*mmit: Grown-Up Sketch Pages for Calm Nights

2) A swear word may appear on the cover, however it should similar to some of the examples included.

3) I'd prefer the background be in black or white so that the picture and color "pop" off the page more.

I've included 4 example covers that I really like. Something similar to these is preferred.

Target Market(s)

Adults age 25-65

Industry/Entity Type

Publishing Company

Font styles to use
Decorative
Script

Requirements
Must have
• Colorful cover with black or white background.
Should not have
• No Slurs, or homophobic language -

```html
<!DOCTYPE html>
<html lang="en">
<head>
<meta charset="utf-8">
<title>Hush Up and Shade, D*mmit — Cover Spread</title>
<link rel="stylesheet" href="https://fonts.googleapis.com/css2?family=Ribeye&family=Marcellus&family=Oswald:wght@400&display=swap">
<style>
  :root {
    --paper: #fbf8e8;
    --paisley-tint: #efe8cc;
    --title-red: #8b1010;
    --ink: #1a1a1a;
    --crimson: #c8174f;
    --teal: #1a8aa6;
    --tan: #e6b86a;
  }
  html, body {
    margin: 0;
    padding: 0;
    width: 1200px;
    height: 862px;
    overflow: hidden;
  }
  .cover-spread {
    position: relative;
    width: 1200px;
    height: 862px;
    background: var(--paper);
    overflow: hidden;
  }
  .paisley-background {
    position: absolute;
    inset: 0;
    background: radial-gradient(circle at 50% 50%, var(--paper) 0%, var(--paisley-tint) 140%);
  }
  .back-cover {
    position: absolute;
    left: 0;
    top: 0;
    width: 570px;
    height: 862px;
  }
  .spine {
    position: absolute;
    left: 570px;
    top: 0;
    width: 62px;
    height: 862px;
  }
  .front-cover {
    position: absolute;
    left: 632px;
    top: 0;
    width: 568px;
    height: 862px;
  }
  .book-title {
    font-family: "Ribeye", cursive;
    color: var(--title-red);
    text-align: center;
    margin: 0;
    font-weight: 400;
    white-space: nowrap;
  }
  .book-subtitle {
    font-family: "Marcellus", serif;
    color: var(--ink);
    text-align: center;
    text-transform: uppercase;
    margin: 0;
    font-weight: 400;
    white-space: nowrap;
  }
  .back-cover .book-title {
    position: absolute;
    left: 0;
    width: 614px;
    top: 244px;
    font-size: 35px;
    line-height: 42px;
  }
  .back-cover .book-subtitle {
    position: absolute;
    left: 0;
    width: 614px;
    top: 336px;
    font-size: 19px;
    line-height: 23px;
    letter-spacing: 0.5px;
  }
  .front-cover .book-title {
    position: absolute;
    left: 0;
    width: 568px;
    top: 238px;
    font-size: 54px;
    line-height: 66px;
  }
  .front-cover .book-subtitle {
    position: absolute;
    left: 6px;
    width: 568px;
    top: 396px;
    font-size: 29px;
    line-height: 37px;
    letter-spacing: 1px;
  }
  .spine-title {
    position: absolute;
    left: 14px;
    top: 150px;
    writing-mode: vertical-rl;
    font-family: "Oswald", sans-serif;
    font-size: 26px;
    letter-spacing: 3px;
    color: var(--title-red);
    text-transform: uppercase;
    white-space: nowrap;
  }
  .ornament {
    position: absolute;
  }
  .ornament-top {
    left: 153px;
    top: 0;
    width: 415px;
    height: 215px;
    border-bottom-left-radius: 60% 100%;
    background: radial-gradient(ellipse at 70% 20%, var(--crimson) 0%, var(--tan) 45%, var(--teal) 100%);
  }
  .ornament-bottom {
    left: 0;
    top: 480px;
    width: 310px;
    height: 382px;
    border-top-right-radius: 100% 60%;
    background: radial-gradient(ellipse at 25% 40%, var(--teal) 0%, var(--tan) 45%, var(--crimson) 100%);
  }
</style>
</head>
<body>
  <main class="cover-spread">
    <div class="paisley-background" role="img" aria-label="Faint cream paisley pattern covering the whole spread"></div>

    <section class="back-cover">
      <h2 class="book-title">Hush Up and<br>Shade, D*mmit</h2>
      <p class="book-subtitle">Grown-Up Sketch Pages<br>for Calm Nights</p>
    </section>

    <section class="spine">
      <span class="spine-title">Hush Up and Shade, D*mmit</span>
    </section>

    <section class="front-cover">
      <div class="ornament ornament-top" role="img" aria-label="Colorful floral mandala ornament in crimson, teal and tan, top corner"></div>
      <h1 class="book-title">Hush Up and<br>Shade, D*mmit</h1>
      <p class="book-subtitle">Grown-Up Sketch Pages<br>for Calm Nights</p>
      <div class="ornament ornament-bottom" role="img" aria-label="Colorful paisley flower ornament in crimson, teal and tan, bottom left of front cover"></div>
    </section>
  </main>
</body>
</html>
```